Letterhead Design Project

Letterhead for a Consultant Cardiologist in Adelaide Australia. Should be very classy, mature and imposing. I would prefer colours that portray confidence, gentleness and serenity.

The PDF attached is for you to see the details that will be on the letterhead and not the design which is extremely poor!

Target Market(s)

Health professionals especially medical doctors

Industry/Entity Type

Consultant

```html
<!DOCTYPE html>
<html lang="en">
<head>
<meta charset="utf-8">
<title>Dr. Emeka T. Okonkwo — Consultant Cardiologist Letterhead</title>
<link rel="stylesheet" href="https://fonts.googleapis.com/css2?family=PT+Sans:wght@400;700&family=Cinzel:wght@400;700&family=Alegreya+SC:wght@500&display=swap">
<style>
  :root {
    --slate: #4a6074;
    --sky: #6fc9ee;
    --ink: #2e3e4c;
    --heading-blue: #1f6fa3;
    --body-ink: #222;
    --paper: #ffffff;
  }
  html, body {
    margin: 0;
    padding: 0;
    overflow: hidden;
    background: var(--paper);
  }
  .letterhead {
    position: relative;
    width: 927px;
    height: 1200px;
    overflow: hidden;
    background: var(--paper);
  }
  .sidebar-top {
    position: absolute;
    left: 0; top: 0;
    width: 187px; height: 985px;
    background: var(--slate);
  }
  .sidebar-bottom {
    position: absolute;
    left: 0; top: 1153px;
    width: 187px; height: 47px;
    background: var(--slate);
  }
  .identity {
    position: absolute;
    left: 80px; top: 60px;
    height: 432px;
    writing-mode: vertical-rl;
    transform: rotate(180deg);
    white-space: nowrap;
  }
  .identity__name {
    display: block;
    font-family: "PT Sans", sans-serif;
    font-weight: 700;
    font-size: 33px;
    line-height: 38px;
    color: var(--paper);
    letter-spacing: -0.3px;
  }
  .identity__title {
    display: block;
    line-height: 26px;
  }
  .identity__role {
    font-family: "Cinzel", serif;
    font-weight: 400;
    font-size: 25px;
    color: var(--sky);
    letter-spacing: 0.5px;
  }
  .identity__divider {
    display: inline-block;
    width: 2px;
    height: 1px;
    border-left: 1.5px solid var(--ink);
    margin: 6px 0;
    height: 0;
    padding-top: 0;
  }
  .identity__rule {
    display: inline-block;
    width: 18px;
    border-top: 1.5px solid var(--ink);
    margin: 0 6px;
    vertical-align: middle;
  }
  .identity__credentials {
    font-family: "Cinzel", serif;
    font-weight: 700;
    font-size: 12.5px;
    color: var(--ink);
    word-spacing: 5px;
  }
  .brand-dot {
    position: absolute;
    left: 82px; top: 500px;
    width: 70px; height: 70px;
    border-radius: 50%;
    background: var(--sky);
  }
  .role-label {
    position: absolute;
    left: 156px; top: 1000px;
    height: 140px;
    writing-mode: vertical-rl;
    transform: rotate(180deg);
    font-family: "PT Sans", sans-serif;
    font-weight: 700;
    font-size: 29px;
    line-height: 32px;
    color: var(--slate);
    text-align: left;
  }
  .locations {
    position: absolute;
    top: 1006px;
    left: 0;
  }
  .location {
    position: absolute;
    top: 0;
    white-space: nowrap;
  }
  .location--clinic { left: 207px; }
  .location--regional { left: 499px; }
  .location--centre { left: 681px; }
  .location__name {
    margin: 0;
    font-family: "PT Sans", sans-serif;
    font-weight: 700;
    font-size: 14.5px;
    line-height: 16px;
    color: var(--heading-blue);
  }
  .location__details {
    margin: 0;
    font-family: "Alegreya SC", serif;
    font-weight: 500;
    font-size: 13px;
    line-height: 16px;
    color: var(--body-ink);
    font-style: normal;
  }
</style>
</head>
<body>
  <main class="letterhead">
    <div class="sidebar-top"></div>
    <div class="sidebar-bottom"></div>

    <header class="identity">
      <span class="identity__name">Dr. Emeka T. Okonkwo</span>
      <span class="identity__title">
        <span class="identity__role">Cardiologist</span><span class="identity__rule"></span><span class="identity__credentials">M.B.B.S F.M.C.P F.R.A.C.P</span>
      </span>
    </header>
    <div class="brand-dot" aria-hidden="true"></div>

    <div class="role-label">Consultant</div>

    <section class="locations">
      <div class="location location--clinic">
        <h2 class="location__name">Riverside Heart &amp; Specialist Clinic<br>Harbourview Central Private Hospital</h2>
        <address class="location__details">
          14-20 Banksia Road<br>
          Greenfield Vale SA 5190<br>
          T: 8310 4420<br>
          F: 8310 4421<br>
          E: heart@rhsc.example.au<br>
          Provider No: 518260AB
        </address>
      </div>
      <div class="location location--regional">
        <h2 class="location__name">Saltbush Bay Hospital</h2>
        <address class="location__details">
          48 Infirmary Road<br>
          Saltbush Bay 5790<br>
          T: 8655 1200<br>
          F: 8257 3388<br>
          Provider No: 518260CD
        </address>
      </div>
      <div class="location location--centre">
        <h2 class="location__name">The Wattle Specialist Centre</h2>
        <address class="location__details">
          62 Redgum Road<br>
          Kestrel Park SA 5030<br>
          T: 8266 7190<br>
          F: 8257 3388<br>
          Provider No: 518260EF
        </address>
      </div>
    </section>
  </main>
</body>
</html>
```